Webbanner-Design für Beteiligungsunternehmen
Zielgruppe
Ich habe ein kleines Familieninternes Beteiligungsunternehmen welches an verschiedenen Firmen beteiligt ist.
Aufgabenstellung
Ich brauche ein Profilbanner für Facebook und Twitter welches zum einen meine Hauptmarke 'Mertlow Holding' und meine Unternehmen an denen ich beteiligt bin (Geldwacht/Kaldoran Real Estate/ TK Holding/Brivalo) zeigt.

```html
<!DOCTYPE html>
<html lang="de">
<head>
<meta charset="utf-8">
<title>Mertlow Holding – Profilbanner</title>
<link rel="stylesheet" href="https://fonts.googleapis.com/css2?family=Exo+2:wght@500;600&display=swap">
<style>
  :root {
    --page-bg: #ffffff;
    --sky-top: #a7b0c0;
    --ridge-blue: #8190b0;
    --mist: #c6ccd7;
    --valley: #7a86a3;
    --ground: #66708c;
    --band: rgba(64, 72, 96, 0.42);
    --ink: #ffffff;
    --shadow: rgba(0, 0, 0, 0.45);
  }
  * { margin: 0; padding: 0; box-sizing: border-box; }
  html, body {
    width: 1200px; height: 845px; overflow: hidden;
    background: var(--page-bg);
    font-family: "Exo 2", sans-serif;
    color: var(--ink);
  }
  .sheet { position: relative; width: 1200px; height: 845px; }

  .banner {
    position: absolute;
    overflow: hidden;
    box-shadow: 0 6px 18px var(--shadow);
  }
  .banner--facebook { left: 323px; top: 80px;  width: 566px;  height: 215px; }
  .banner--twitter  { left: 89px;  top: 428px; width: 1034px; height: 344px; }

  .landscape {
    position: absolute; inset: 0;
    background: linear-gradient(180deg,
      var(--sky-top) 0%,
      var(--ridge-blue) 28%,
      var(--valley) 42%,
      var(--mist) 62%,
      var(--valley) 78%,
      var(--ground) 100%);
  }

  .brand {
    position: absolute; left: 0; right: 0;
    display: flex; justify-content: center; align-items: center;
    font-weight: 600; text-transform: uppercase;
    white-space: nowrap;
  }
  .brand__mark { background: var(--ink); flex: none; }
  .banner--facebook .brand { top: 44px; height: 80px; font-size: 34px; gap: 12px; letter-spacing: 1px; }
  .banner--facebook .brand__mark { width: 22px; height: 22px; }
  .banner--twitter .brand { top: 70px; height: 130px; font-size: 62px; gap: 22px; letter-spacing: 2px; }
  .banner--twitter .brand__mark { width: 40px; height: 40px; }

  .partners {
    position: absolute; left: 0; right: 0; bottom: 0;
    background: var(--band);
  }
  .banner--facebook .partners { height: 54px; }
  .banner--twitter .partners { height: 100px; }

  .partner {
    position: absolute; top: 50%;
    transform: translate(-50%, -50%);
    display: flex; align-items: center;
    font-weight: 500; text-transform: uppercase;
    white-space: nowrap;
  }
  .partner__dot { background: var(--ink); border-radius: 50%; flex: none; }
  .banner--facebook .partner { font-size: 11px; gap: 5px; letter-spacing: 0.8px; }
  .banner--facebook .partner__dot { width: 8px; height: 8px; }
  .banner--twitter .partner { font-size: 20px; gap: 9px; letter-spacing: 1.5px; }
  .banner--twitter .partner__dot { width: 14px; height: 14px; }

  .banner--facebook .partner--geldwacht { left: 85px; }
  .banner--facebook .partner--kaldoran  { left: 217px; }
  .banner--facebook .partner--tk        { left: 345px; }
  .banner--facebook .partner--brivalo   { left: 471px; }
  .banner--twitter .partner--geldwacht  { left: 155px; }
  .banner--twitter .partner--kaldoran   { left: 398px; }
  .banner--twitter .partner--tk         { left: 629px; }
  .banner--twitter .partner--brivalo    { left: 862px; }
</style>
</head>
<body>
<main class="sheet">

  <section class="banner banner--facebook" aria-label="Facebook-Titelbild">
    <div class="landscape" role="img" aria-label="Nebelige Berglandschaft mit blauen Gebirgsketten"></div>
    <h1 class="brand"><span class="brand__mark"></span>Mertlow Holding</h1>
    <ul class="partners" aria-label="Beteiligungen">
      <li class="partner partner--geldwacht"><span class="partner__dot"></span>Geldwacht</li>
      <li class="partner partner--kaldoran"><span class="partner__dot"></span>Kaldoran Real Estate</li>
      <li class="partner partner--tk"><span class="partner__dot"></span>TK Holding</li>
      <li class="partner partner--brivalo"><span class="partner__dot"></span>Brivalo</li>
    </ul>
  </section>

  <section class="banner banner--twitter" aria-label="Twitter-Header">
    <div class="landscape" role="img" aria-label="Nebelige Berglandschaft mit blauen Gebirgsketten"></div>
    <h2 class="brand"><span class="brand__mark"></span>Mertlow Holding</h2>
    <ul class="partners" aria-label="Beteiligungen">
      <li class="partner partner--geldwacht"><span class="partner__dot"></span>Geldwacht</li>
      <li class="partner partner--kaldoran"><span class="partner__dot"></span>Kaldoran Real Estate</li>
      <li class="partner partner--tk"><span class="partner__dot"></span>TK Holding</li>
      <li class="partner partner--brivalo"><span class="partner__dot"></span>Brivalo</li>
    </ul>
  </section>

</main>
</body>
</html>
```